Webdesign für IT-Dienstleister
Zielgruppe
Seit 1997 bieten wir erstklassige IT-Dienstleistungen Mainz an, die darauf ausgerichtet sind, Unternehmen und Privatkunden mit kompetenter Beratung, zuverlässiger Unterstützung und modernen Technologielösungen zur Seite zu stehen.
Umfassende Computer-Serviceleistungen
Unser Computer-Service Mainz beinhaltet eine Reihe von Dienstleistungen, die darauf abzielen, die Leistungsfähigkeit Ihrer IT-Infrastruktur zu optimieren und zu erhalten. Von der Fehlerdiagnose bis hin zur Wartung bieten wir ein Rundum-Sorglos-Paket für Ihre Hardware und Software.
Professionelle Fehleranalyse und Reparatur
Optimierung von Betriebssystemen und Anwendungen
Regelmäßige Wartungsarbeiten zur Vorbeugung von Ausfällen
Ersetzen und Aufrüsten von Hardware-Komponenten
Aufgabenstellung
Ich hätte gern ein modernes Design. Ein Logo vorhanden, sollte mit eingebaut werden.
Ansonsten hätte ich gerne eine einzelne Webseite mit den Firmen Infos (und den Links zu Sozial Media) und einer extra Impressum Seite. Und wenn möglich noch ein Anfrage Formular.
Am liebsten wäre ein Format welches ich in WordPress verarbeiten werden kann.
(Logo wird noch nachgereicht)

```html
<!DOCTYPE html>
<html lang="de">
<head>
<meta charset="utf-8">
<title>IT-Dienstleistungen Berg – IT-Service</title>
<link href="https://fonts.googleapis.com/css2?family=Outfit:wght@400;500;600&family=Poppins:wght@400;500;600&display=swap" rel="stylesheet">
<style>
:root{
  --navy:#1c2b5a;
  --navy-deep:#14214a;
  --blue:#2f4d92;
  --cyan:#27a9e1;
  --ink:#14171f;
  --muted:#7a7f8c;
  --line:#d9dde5;
  --white:#ffffff;
}
*{margin:0;padding:0;box-sizing:border-box}
html,body{width:1200px;height:4283px;overflow:hidden}
body{font-family:"Poppins",sans-serif;color:var(--ink);background:var(--white);position:relative}
.abs{position:absolute}
h1,h2,h3,.head{font-family:"Outfit",sans-serif;font-weight:400}
.label{font-family:"Outfit",sans-serif;color:var(--cyan);font-size:23px;letter-spacing:-.3px}
.section{position:absolute;left:0;width:1200px}
.img{position:absolute;border-radius:8px}

/* hero */
.hero{top:0;height:675px;background:radial-gradient(circle at 70% 40%,#4a6ea6 0%,#22375f 45%,#0d1a34 100%)}
.nav{left:125px;top:20px;width:950px;height:66px;background:#fff;border-radius:33px}
.logo-name{font-family:"Poppins",sans-serif;font-weight:600;color:var(--navy)}
.nav .logo-name{left:30px;top:18px;font-size:20px}
.nav .logo-dot{left:28px;top:0}
.nav a{position:absolute;top:26px;font-size:11px;color:#555;text-decoration:none}
.nav a.active{color:var(--ink);font-weight:600}
.hero h1{left:150px;top:205px;font-size:72px;font-weight:600;color:#fff;letter-spacing:1px}
.hero .sub{left:151px;top:298px;font-size:19px;color:#fff}
.hero .intro{left:151px;top:352px;width:370px;font-size:9.5px;line-height:17px;color:#e4e9f3}
.btn-white{background:#fff;color:var(--ink);font-size:12px;font-weight:500;border-radius:5px;display:flex;align-items:center;justify-content:center}
.avatar{position:absolute;width:46px;height:46px;border-radius:50%;border:3px solid #fff}
.hero .cs{left:316px;top:536px;font-size:16px;color:#fff}
.pill{position:absolute;left:821px;width:229px;height:28px;border:1px solid rgba(255,255,255,.7);border-radius:14px;color:#fff;font-size:9.5px;padding:8px 12px;background:rgba(255,255,255,.06)}
.pill span{position:absolute;right:14px;top:5px;font-size:11px}
.hw-card{left:821px;top:382px;width:229px;height:87px;background:#fff;border-radius:14px;padding:12px 12px}
.hw-card b{font-size:11px;font-weight:600}
.hw-card li{font-size:8px;color:#333;margin-left:14px;line-height:13px}

/* about */
.about{top:675px;height:796px}
.center{text-align:center;width:1200px;left:0}
.title{font-size:36px;line-height:50px;color:var(--ink);letter-spacing:-.5px}
.exp{left:151px;top:1283px;width:286px;height:95px;background:var(--navy);border-radius:6px;color:#fff;text-align:center;padding-top:15px}
.exp .num{font-family:"Outfit",sans-serif;font-size:38px;line-height:40px}
.exp .cap{font-size:15px}
.body{font-size:9.5px;line-height:18px;color:var(--muted)}
.checks{list-style:none}
.checks li{font-size:9.5px;color:var(--muted);display:flex;align-items:center;gap:10px}
.btn-cyan{background:var(--cyan);color:#fff;font-size:12px;font-weight:500;border-radius:5px;display:flex;align-items:center;justify-content:center}

/* services */
.services{top:1471px;height:716px;background:radial-gradient(ellipse at 50% 80%,#3a5da4 0%,#223a78 55%,#1b2e62 100%)}
.services .label,.testi .label{color:#fff}
.services .title,.testi .title{color:#fff}
.card{position:absolute;width:287px;background:#fff;border-radius:8px;overflow:hidden}
.card .photo{height:183px}
.card .icon{position:absolute;right:40px;top:158px;width:50px;height:50px;border-radius:50%;background:#fff;border:3px solid #e4e7ef;display:flex;align-items:center;justify-content:center}
.card h3{position:absolute;left:17px;top:210px;font-size:19px;line-height:23px;color:var(--cyan)}
.card p{position:absolute;left:17px;top:264px;width:255px;font-size:8.8px;line-height:18px;color:#777}
.card p em{font-style:normal;color:var(--cyan)}
.card p i{font-style:normal;color:#e0556b}

/* why */
.why{top:2187px;height:692px}
.feat{position:absolute;left:645px;width:146px;height:124px;background:#fff;box-shadow:0 4px 18px rgba(20,30,60,.12);text-align:center;font-size:15px;line-height:18px;color:var(--ink);padding-top:14px}
.feat svg{display:block;margin:0 auto 6px}
.feat.on{background:var(--cyan);color:#fff}

/* testimonials */
.testi{top:2879px;height:556px;background:radial-gradient(ellipse at 50% 100%,#3c5fa8 0%,#22397a 60%,#1d3068 100%)}
.tcard{position:absolute;top:3070px;width:287px;height:307px;background:#fff;border-radius:8px;text-align:center}
.tcard .q{font-family:"Outfit",sans-serif;font-weight:600;font-size:90px;line-height:80px;color:var(--navy);margin-top:22px;height:55px}
.tcard p{font-size:9px;line-height:18px;color:#444;padding:0 28px;margin-top:6px}
.tcard .face{width:70px;height:70px;border-radius:50%;margin:18px auto 0}
.tcard .n{font-size:15px;margin-top:8px}
.tcard .r{font-size:10px;font-weight:600}

/* contact */
.contact{top:3435px;height:521px}
.field{position:absolute;height:38px;border:1px solid var(--line);border-radius:4px;font-size:11px;color:#888;padding:11px 16px}
.cinfo b{font-weight:500;font-size:14px;display:block}
.cinfo small{font-size:9px;color:#777}

/* footer */
.footer{top:3956px;height:327px;background:var(--navy-deep)}
.footer .col-h{font-family:"Outfit",sans-serif;font-size:19px;color:#fff;line-height:24px}
.footer .link{font-size:9.5px;color:#d5dbe9;line-height:13px}
.footer p{font-size:9px;color:#d5dbe9;line-height:16px}
</style>
</head>
<body>

<!-- HERO -->
<section class="section hero" role="img" aria-label="Zwei Techniker im Rechenzentrum, blau getöntes Foto"></section>
<nav class="abs nav">
  <svg class="abs logo-dot" width="0" height="0"></svg>
  <span class="abs" style="left:28px;top:20px;width:20px;height:20px;border-radius:50%;background:var(--navy)"></span>
  <span class="abs logo-name" style="left:58px;top:20px;font-size:18px">netzwerk-hilfe.de</span>
  <a class="active" style="left:298px">Heim</a>
  <a style="left:350px">Über Uns</a>
  <a style="left:420px">Unsere Leistungen ⌄</a>
  <a style="left:555px">Warum wählen uns</a>
  <a style="left:678px">Kontaktinformationen</a>
  <svg class="abs" style="left:826px;top:23px" width="20" height="20" viewBox="0 0 20 20"><circle cx="8" cy="8" r="6" fill="none" stroke="#111" stroke-width="2"/><path d="M12.5 12.5 18 18" stroke="#111" stroke-width="2"/></svg>
  <svg class="abs" style="left:868px;top:22px" width="20" height="22" viewBox="0 0 20 22"><path d="M4 15V9a6 6 0 0 1 12 0v6l2 2H2z" fill="none" stroke="#111" stroke-width="2"/><circle cx="10" cy="19.5" r="2" fill="#111"/></svg>
  <svg class="abs" style="left:910px;top:22px" width="22" height="22" viewBox="0 0 22 22"><circle cx="11" cy="11" r="9" fill="none" stroke="#111" stroke-width="2"/><circle cx="11" cy="9" r="3" fill="none" stroke="#111" stroke-width="2"/><path d="M5 17c3-3 9-3 12 0" fill="none" stroke="#111" stroke-width="2"/></svg>
</nav>
<h1 class="abs" style="left:150px;top:205px;font-size:72px;font-weight:600;color:#fff;letter-spacing:1px;font-family:'Poppins',sans-serif">IT-Service</h1>
<div class="abs" style="left:151px;top:298px;font-size:19px;color:#fff">Dem Sie Vertrauen Können – Seit 1997</div>
<div class="abs" style="left:151px;top:352px;width:370px;font-size:9.5px;line-height:17px;color:#e4e9f3">With A Sleek And Modern Aesthetic, Your Landing Page Resonates With Ambition And Professionalism, Emphasizing Innovation As The Cornerstone Of Success.</div>
<div class="abs btn-white" style="left:151px;top:425px;width:148px;height:33px">Erfahren Sie mehr</div>
<div class="avatar" role="img" aria-label="Kundenporträt" style="left:316px;top:472px;background:#8a7a6c"></div>
<div class="avatar" role="img" aria-label="Kundenporträt" style="left:352px;top:472px;background:#b79a80"></div>
<div class="avatar" role="img" aria-label="Kundenporträt" style="left:388px;top:472px;background:#6e7f96"></div>
<div class="avatar" role="img" aria-label="Kundenporträt" style="left:424px;top:472px;background:#a08772"></div>
<div class="abs" style="left:316px;top:536px;font-size:16px;color:#fff">Client Satisfaction</div>
<div class="pill" style="top:283px">Professionelle Fehleranalyse<span>→</span></div>
<div class="pill" style="top:316px">Regelmäßige Wartungsarbeiten<span>↪</span></div>
<div class="pill" style="top:349px">Optimierung von Betriebssystemen<span>↪</span></div>
<div class="abs hw-card"><b>Hardware-Komponenten</b><ul style="margin-top:6px"><li>Old hardware ka replacement</li><li>New components ka upgrade<br>(e.g., RAM, SSD, graphics card)</li></ul></div>

<!-- ABOUT -->
<section class="section about"></section>
<div class="abs center label" style="top:767px">ÜBER UNS</div>
<h2 class="abs center title" style="top:801px">Seit 1997 Ihr Partner Für<br>Zuverlässige IT-Lösungen</h2>
<div class="img" role="img" aria-label="Zwei Techniker vor einem Serverschrank" style="left:151px;top:941px;width:286px;height:322px;background:linear-gradient(160deg,#b9c3cf,#5e6f86)"></div>
<div class="abs exp"><div class="num">12+</div><div class="cap">Jahre Erfahrung</div></div>
<div class="abs" style="left:457px;top:943px;font-size:15px;font-weight:500">Regelmäßige Wartungsarbeiten</div>
<div class="abs body" style="left:457px;top:974px;width:310px">Lorem Ipsum Dolor Sit Amet Consectetur. Velit Tortor Molestie Praesent Est Eget Etiam Consequat. Nibh Tristique Vel Ut Hac Odio Ut Tem Tempor Turpis. Et Penatibus Ornare Neque Hendrerit Mauris Rhoncus Lectus. Lectus Nisl Quam.</div>
<div class="abs btn-cyan" style="left:457px;top:1070px;width:146px;height:42px">Erfahren Sie Mehr</div>
<ul class="abs checks" style="left:821px;top:972px">
  <li style="height:31px"><svg width="16" height="16" viewBox="0 0 16 16"><circle cx="8" cy="8" r="8" fill="var(--navy)"/><path d="M4.5 8.2 7 10.5l4.5-5" stroke="#fff" stroke-width="1.6" fill="none"/></svg>Blandit Nec Id Sit Sapien Bibendum Nisi.</li>
  <li style="height:31px"><svg width="16" height="16" viewBox="0 0 16 16"><circle cx="8" cy="8" r="8" fill="var(--navy)"/><path d="M4.5 8.2 7 10.5l4.5-5" stroke="#fff" stroke-width="1.6" fill="none"/></svg>Lorem Ipsum Dolor Sit Amet</li>
  <li style="height:31px"><svg width="16" height="16" viewBox="0 0 16 16"><circle cx="8" cy="8" r="8" fill="var(--navy)"/><path d="M4.5 8.2 7 10.5l4.5-5" stroke="#fff" stroke-width="1.6" fill="none"/></svg>Lorem Ipsum Dolor</li>
  <li style="height:31px"><svg width="16" height="16" viewBox="0 0 16 16"><circle cx="8" cy="8" r="8" fill="var(--navy)"/><path d="M4.5 8.2 7 10.5l4.5-5" stroke="#fff" stroke-width="1.6" fill="none"/></svg>Lorem Ipsum Dolor</li>
</ul>
<div class="img" role="img" aria-label="Team arbeitet gemeinsam an Computern, blau getönt" style="left:457px;top:1145px;width:593px;height:233px;background:linear-gradient(120deg,#9fb3cc,#3f5b86 60%,#6d8bb5)"></div>

<!-- SERVICES -->
<section class="section services"></section>
<div class="abs center label" style="top:1531px">UNSERE LEISTUNGEN</div>
<h2 class="abs center title" style="top:1565px;font-size:34px">IT-Services, Die Ihre Technik Am Laufen Halten</h2>
<div class="card" style="left:151px;top:1664px;height:384px">
  <div class="photo" role="img" aria-label="Netzwerk-Switch mit blauen Kabeln" style="background:linear-gradient(180deg,#2b3140,#4aa6d9 70%,#1d2330)"></div>
  <div class="icon"><svg width="22" height="22" viewBox="0 0 22 22"><rect x="3" y="4" width="16" height="11" rx="1" fill="none" stroke="var(--blue)" stroke-width="2"/><path d="M8 19h6M11 15v4" stroke="var(--blue)" stroke-width="2"/></svg></div>
  <h3>Computernetzwerk-<br>Dienstleistungen</h3>
  <p>Lorem Ipsum Dolor Sit Amet Consectetur. V Tortor Molestie Praesent <em>Est Eget Etia Consequat.</em> Nibh Tristique Vel Ut Hac Odio Ut Tem TurpisLore Ipsum Dolor Sit Amet Consectetur. <i>Velit Tort Mol</i> Praesent Est <em>Eget Etiam Consequat.</em> Nibh Tristique Vel Ut Hac Odio Ut Tempor Turpis.</p>
</div>
<div class="card" style="left:457px;top:1664px;height:384px">
  <div class="photo" role="img" aria-label="Techniker repariert ein Gerät" style="background:linear-gradient(180deg,#dfe7ef,#7fa7cc)"></div>
  <div class="icon"><svg width="22" height="22" viewBox="0 0 22 22"><circle cx="9" cy="9" r="6" fill="none" stroke="var(--blue)" stroke-width="2"/><path d="M13.5 13.5 19 19" stroke="var(--blue)" stroke-width="2.5"/></svg></div>
  <h3>Service &amp;<br>Wartungsverträge</h3>
  <p>Lorem Ipsum Dolor Sit Amet Consectetur. V Tortor Molestie Praesent <em>Est Eget Etia Consequat.</em> Nibh Tristique Vel Ut Hac Odio Ut Tem TurpisLore Ipsum Dolor Sit Amet Consectetur. <i>Velit Tort Mol</i> Praesent Est <em>Eget Etiam Consequat.</em> Nibh Tristique Vel Ut Hac Odio Ut Tempor Turpis.</p>
</div>
<div class="card" style="left:763px;top:1664px;height:384px">
  <div class="photo" role="img" aria-label="Mann mit Laptop vor blauem Hintergrund" style="background:linear-gradient(180deg,#5ba9de,#a7d3f0)"></div>
  <div class="icon"><svg width="22" height="22" viewBox="0 0 22 22"><rect x="3" y="11" width="16" height="6" rx="1" fill="none" stroke="var(--blue)" stroke-width="2"/><path d="M7 11V5M15 11V5" stroke="var(--blue)" stroke-width="2"/></svg></div>
  <h3>DSL &amp; Internet<br>Produkte</h3>
  <p>Lorem Ipsum Dolor Sit Amet Consectetur. V Tortor Molestie Praesent <em>Est Eget Etia Consequat.</em> Nibh Tristique Vel Ut Hac Odio Ut Tem TurpisLore Ipsum Dolor Sit Amet Consectetur. <i>Velit Tort Mol</i> Praesent Est <em>Eget Etiam Consequat.</em> Nibh Tristique Vel Ut Hac Odio Ut Tempor Turpis.</p>
</div>
<div class="abs btn-white" style="left:520px;top:2087px;width:160px;height:40px">Entdecken Sie Mehr</div>

<!-- WHY US -->
<section class="section why"></section>
<div class="abs label" style="left:151px;top:2354px">WARUM WÄHLEN UNS</div>
<h2 class="abs title" style="left:151px;top:2387px">Weil Ihre IT Nur Den Besten<br>Service Verdient</h2>
<div class="abs body" style="left:151px;top:2502px;width:440px;font-size:9px">Lorem Ipsum Dolor Sit Amet Consectetur. Velit Tortor Molestie Praesent Est Eget Etiam Consequat. Nibh Tristique Vel Ut Hac Odio Ut Tempor Turpis. Et Penatibus Ornare Neque Hendrerit Mauris Rhoncus Lectus. Lectus N</div>
<ul class="abs checks" style="left:151px;top:2578px">
  <li style="height:25px"><svg width="15" height="15" viewBox="0 0 16 16"><circle cx="8" cy="8" r="8" fill="var(--cyan)"/><path d="M4.5 8.2 7 10.5l4.5-5" stroke="#fff" stroke-width="1.6" fill="none"/></svg>Blandit Nec Id Sit Sapien Bibendum Nisi.</li>
  <li style="height:25px"><svg width="15" height="15" viewBox="0 0 16 16"><circle cx="8" cy="8" r="8" fill="var(--cyan)"/><path d="M4.5 8.2 7 10.5l4.5-5" stroke="#fff" stroke-width="1.6" fill="none"/></svg>Lorem Ipsum Dolor Sit Amet</li>
  <li style="height:25px"><svg width="15" height="15" viewBox="0 0 16 16"><circle cx="8" cy="8" r="8" fill="var(--cyan)"/><path d="M4.5 8.2 7 10.5l4.5-5" stroke="#fff" stroke-width="1.6" fill="none"/></svg>Lorem Ipsum Dolor</li>
</ul>
<div class="abs" style="left:151px;top:2676px;font-size:12px;font-weight:500">Regelmäßige Wartungsarbeiten</div>
<div class="abs" style="left:491px;top:2667px;width:26px;height:18px;background:var(--navy-deep);color:#fff;font-size:7px;text-align:center;line-height:18px;border-radius:2px">100</div>
<div class="abs" style="left:151px;top:2703px;width:365px;height:9px;background:var(--navy);border-radius:5px"></div>
<div class="img" role="img" aria-label="Geschäftsmann mit Headset und Tablet vor blauem Technik-Hintergrund" style="left:718px;top:2282px;width:332px;height:502px;background:linear-gradient(150deg,#4a8fd6,#1e3f86 60%,#0f2152)"></div>
<div class="feat" style="top:2327px"><svg width="34" height="34" viewBox="0 0 34 34"><circle cx="17" cy="17" r="14" fill="none" stroke="var(--navy)" stroke-width="2"/><path d="M17 8v9l5 4" stroke="var(--navy)" stroke-width="2.5" fill="none"/></svg>Erfahrung seit<br>1997</div>
<div class="feat on" style="top:2471px"><svg width="34" height="40" viewBox="0 0 34 40"><path d="M20 2 6 22h10l-4 16 16-22H18z" fill="#fff"/></svg>Schnelle &amp;<br>Zuverlässige Hilfe</div>
<div class="feat" style="top:2614px"><svg width="38" height="38" viewBox="0 0 38 38"><path d="M26 4a8 8 0 0 0-8 11L5 28l5 5 13-13a8 8 0 0 0 11-8l-5 5-5-1-1-5z" fill="var(--navy)"/></svg>Kompetente<br>Beratung</div>

<!-- TESTIMONIALS -->
<section class="section testi"></section>
<div class="abs center label" style="top:2937px">TESTIMONIALS</div>
<h2 class="abs center title" style="top:2970px;font-size:36px">Was Unsere Kunden Über Uns Sagen</h2>
<div class="tcard" style="left:151px"><div class="q">“</div><p>Lorem Ipsum Dolor Sit Amet Consectetur. Velit Ultricies Et Faucibus Tortor Suspendisse Id Auctor. Integer Commodo Eget At Nec Nisl Amet. Rhoncus Egestas Pharetra Mi Ipsum.</p><div class="face" role="img" aria-label="Kundenfoto" style="background:#8f7a68"></div><div class="n">Lukas Brandt</div><div class="r">Jana Hoffmann</div></div>
<div class="tcard" style="left:457px"><div class="q">“</div><p>Lorem Ipsum Dolor Sit Amet Consectetur. Velit Ultricies Et Faucibus Tortor Suspendisse Id Auctor. Integer Commodo Eget At Nec Nisl Amet. Rhoncus Egestas Pharetra Mi Ipsum.</p><div class="face" role="img" aria-label="Kundenfoto" style="background:#6d6a69"></div><div class="n">Lukas Brandt</div><div class="r">Global Directives Architect</div></div>
<div class="tcard" style="left:763px"><div class="q">“</div><p>Lorem Ipsum Dolor Sit Amet Consectetur. Velit Ultricies Et Faucibus Tortor Suspendisse Id Auctor. Integer Commodo Eget At Nec Nisl Amet. Rhoncus Egestas Pharetra Mi Ipsum.</p><div class="face" role="img" aria-label="Kundenfoto" style="background:#9aa27e"></div><div class="n">Lukas Brandt</div><div class="r">Felix Bauer</div></div>

<!-- CONTACT -->
<section class="section contact"></section>
<div class="abs label" style="left:151px;top:3532px">CONTACT US</div>
<h2 class="abs title" style="left:151px;top:3563px">Wir Sind Nur Einen<br>Klick Entfernt</h2>
<div class="abs body" style="left:151px;top:3682px;width:355px;font-size:10.5px;line-height:21px">Lorem Ipsum Dolor Sit Amet, Consectetur. Pellentesque Velit Pellentesque Euismod Accumsan Egestas Cursus. Id Diam Augue Consequat Diam.</div>
<div class="abs cinfo" style="left:151px;top:3772px;display:flex;gap:12px"><svg width="30" height="24" viewBox="0 0 30 24"><rect x="2" y="3" width="26" height="18" rx="2" fill="none" stroke="var(--navy)" stroke-width="2.5"/><path d="M3 5l12 9 12-9" fill="none" stroke="var(--navy)" stroke-width="2.5"/></svg><div><b>E-Mail</b><small>kontakt@beispiel-it.de</small></div></div>
<div class="abs cinfo" style="left:387px;top:3772px;display:flex;gap:12px"><svg width="30" height="30" viewBox="0 0 30 30"><path d="M7 3l5 6-3 3c2 4 5 7 9 9l3-3 6 5-3 4C13 26 4 17 3 6z" fill="none" stroke="var(--navy)" stroke-width="2.2"/></svg><div><b>Anruf</b><small>(0000) 123-4567</small></div></div>
<div class="abs cinfo" style="left:151px;top:3826px;display:flex;gap:12px"><svg width="26" height="30" viewBox="0 0 26 30"><path d="M13 28S3 17 3 11a10 10 0 0 1 20 0c0 6-10 17-10 17z" fill="none" stroke="var(--navy)" stroke-width="2.4"/><circle cx="13" cy="11" r="3.5" fill="none" stroke="var(--navy)" stroke-width="2.2"/></svg><div><b>Adresse</b><small>Musterweg 12, 55000 Beispielstadt</small></div></div>
<div class="field" style="left:530px;top:3532px;width:251px">Name</div>
<div class="field" style="left:799px;top:3532px;width:251px">Telefonnummer</div>
<div class="field" style="left:530px;top:3588px;width:251px">E-Mail-Adresse</div>
<div class="field" style="left:799px;top:3588px;width:251px">Dienstleistungen<span style="position:absolute;right:16px;top:8px;color:#333">⌄</span></div>
<div class="field" style="left:530px;top:3645px;width:520px;height:144px">Nachrichten</div>
<div class="abs btn-cyan" style="left:530px;top:3813px;width:520px;height:39px">Einreichen ↗</div>

<!-- FOOTER -->
<section class="section footer"></section>
<span class="abs" style="left:151px;top:4050px;width:30px;height:30px;border-radius:50%;background:#fff"></span>
<span class="abs logo-name" style="left:192px;top:4052px;font-size:20px;color:#fff">netzwerk-hilfe.de</span>
<p class="abs" style="left:151px;top:4098px;width:270px">Lorem Ipsum Dolor Sit Amet, Consectetur Adipiscing Elit, Sed Do Eiu TemporLorem Ipsum Dolor Sit Amet</p>
<div class="abs col-h" style="left:459px;top:4042px">Über uns</div>
<div class="abs link" style="left:459px;top:4098px">Paul Winter</div>
<div class="abs link" style="left:459px;top:4124px">Sara Keller</div>
<div class="abs link" style="left:459px;top:4151px">Mia Lorenz</div>
<div class="abs col-h" style="left:609px;top:4042px">Unsere<br>Leistungen</div>
<div class="abs link" style="left:609px;top:4113px">Tim Vogel</div>
<div class="abs link" style="left:609px;top:4140px">Nico Hahn</div>
<div class="abs link" style="left:609px;top:4167px">Ben Wolff</div>
<div class="abs link" style="left:609px;top:4194px">Erik Sommer</div>
<div class="abs col-h" style="left:778px;top:4042px">Newsletter</div>
<p class="abs" style="left:771px;top:4078px;width:290px">Lorem Ipsum Dolor Sit Amet, Consectetur Adipiscing Elit, Sed Do Eiusmod TemporLorem Ipsum Dolor</p>
<div class="abs" style="left:771px;top:4142px;width:171px;height:38px;background:#fff;border-radius:4px;font-size:11px;color:#888;padding:11px 18px">E-Mail</div>
<div class="abs" style="left:956px;top:4142px;width:96px;height:38px;border:1px solid #fff;border-radius:4px;font-size:12px;color:#fff;text-align:center;line-height:36px">Abonnieren</div>
<div class="abs" style="left:62px;top:4230px;width:1076px;height:1px;background:rgba(255,255,255,.3)"></div>
<div class="abs center" style="top:4250px;font-size:9px;color:#d5dbe9">Copyright © 2025 Berg IT.</div>

</body>
</html>
```